Healthy Supplement featuring Moringa products

Need 3 business card options for our reps to order from Printwell. Our reps will be ordering from Printwell once we upload them. Attached is our current designs to show what info needs to be on the cards. Our website is www.tqvitality.com
The business cards will be a template for our reps to order from. Most of our reps are Asian & Hispanic. Please look at our website so you can see who we are to get the look and feel what we need.
Target Market(s)
Adults 30 on up. Health oriented people.
Industry/Entity Type
Health And Wellness
Contact Information for Business Card
Name
Title
Phone
Logo
www.tqvitality.com/my/username
Font styles to use
Requirements
Must have
- Please match our website look and colors. A moringa leaf is nice, but am open to something different.
Nice to have
- Healthy looking and warm, not super cold or too modern.
Should not have
- No harsh colors please.

```html
<!DOCTYPE html>
<html lang="en">
<head>
<meta charset="UTF-8">
<title>TQ Vitality Business Card</title>
<link rel="stylesheet" href="https://fonts.googleapis.com/css2?family=Oswald:wght@500&family=Work+Sans:wght@400;500&display=swap">
<style>
  :root {
    --page: #2a2a2a;
    --card: #1e1e1e;
    --card-edge: #262626;
    --green: #8cc63f;
    --white: #f2f2f2;
    --silver: #c9c9c9;
  }
  * { box-sizing: border-box; margin: 0; padding: 0; }
  html, body {
    width: 1200px; height: 900px; overflow: hidden;
    background: var(--page);
    font-family: "Work Sans", sans-serif;
  }
  .canvas {
    width: 1200px; height: 900px;
    display: flex; flex-direction: column; align-items: center; justify-content: center;
    gap: 40px;
  }
  .card {
    position: relative;
    width: 630px; height: 360px;
    background: linear-gradient(135deg, var(--card-edge), var(--card));
    box-shadow: 0 10px 24px rgba(0,0,0,0.45);
  }
  /* Front */
  .card-front { display: flex; align-items: center; justify-content: center; }
  .brand {
    display: flex; align-items: center; gap: 14px;
    font-family: "Work Sans", sans-serif; font-weight: 500;
    font-size: 44px; letter-spacing: 3px; color: var(--silver);
  }
  .brand-dot { width: 18px; height: 18px; border-radius: 50%; background: var(--silver); }
  /* Back */
  .identity {
    position: absolute; right: 352px; top: 128px; text-align: right;
  }
  .name {
    font-family: "Oswald", sans-serif; font-weight: 500;
    font-size: 38px; line-height: 1; color: var(--green); letter-spacing: 0.5px;
    text-transform: uppercase;
  }
  .title { font-size: 15px; color: var(--white); margin-top: 4px; }
  .divider {
    position: absolute; left: 300px; top: 118px; width: 2px; height: 84px;
    background: var(--green);
  }
  .contacts {
    position: absolute; left: 322px; top: 118px; list-style: none;
    font-size: 16px; color: var(--white); line-height: 21px;
  }
  .contacts li { display: flex; align-items: center; gap: 9px; }
  .contacts svg { width: 11px; height: 11px; flex: none; }
  .address {
    position: absolute; left: 112px; top: 290px;
    font-size: 16px; color: var(--white);
  }
</style>
</head>
<body>
<main class="canvas">
  <section class="card card-front">
    <div class="brand"><span class="brand-dot"></span>TQ VITALITY</div>
  </section>

  <section class="card card-back">
    <div class="identity">
      <div class="name">Daniel Reyes</div>
      <div class="title">Director</div>
    </div>
    <div class="divider"></div>
    <ul class="contacts">
      <li>
        <svg viewBox="0 0 12 12"><path d="M3 1l2 2.5-1.2 1.2a7 7 0 0 0 3.5 3.5L8.5 7 11 9l-1 2C5 11 1 7 1 2z" fill="var(--green)"/></svg>
        555 214-3870
      </li>
      <li>
        <svg viewBox="0 0 12 12"><rect x="3" y="1" width="6" height="3" fill="var(--green)"/><rect x="1" y="4" width="10" height="5" rx="1" fill="var(--green)"/><rect x="3" y="8" width="6" height="3" fill="var(--green)"/></svg>
        555 214-3871
      </li>
      <li>
        <svg viewBox="0 0 12 12"><rect x="1" y="2.5" width="10" height="7" fill="none" stroke="var(--green)" stroke-width="1.2"/><path d="M1 2.5l5 4 5-4" fill="none" stroke="var(--green)" stroke-width="1.2"/></svg>
        info@tqvitality.com
      </li>
      <li>
        <svg viewBox="0 0 12 12"><circle cx="6" cy="6" r="5" fill="none" stroke="var(--green)" stroke-width="1.2"/><path d="M1 6h10M6 1c-2.5 3-2.5 7 0 10M6 1c2.5 3 2.5 7 0 10" fill="none" stroke="var(--green)" stroke-width="1"/></svg>
        www.tqvitality.com
      </li>
    </ul>
    <p class="address">418 Orchard Ave. STE B Fairview, CA 90412</p>
  </section>
</main>
</body>
</html>
```